Brookside Grocer

Hope all is well!

Wanted to make business cards for my father. His name is Faisal Qureshi and owns convenience stores. I have attached logo :)

He does not want any title just simple name and phone. An email would be nice as well.

Faisal Qureshi
Cell: 413-585-2046
Store: 413-719-4820

Brooksidegrocer512@fernpost.com

The design and style is totally up to you :) The colors we were looking for were the same as logo :)

```html
<!DOCTYPE html>
<html lang="en">
<head>
<meta charset="utf-8">
<title>Brookside Grocer — Business Card</title>
<link href="https://fonts.googleapis.com/css2?family=Lato:wght@400;700;900&display=swap" rel="stylesheet">
<style>
  :root {
    --page-bg: #ecebee;
    --navy-deep: #15225a;
    --navy-mid: #2a3a72;
    --navy-soft: #56628f;
    --panel-light: #e4e2e7;
    --ring-white: #f4f3f6;
    --disc-grey: #b9bccb;
    --name-cream: #ece0cd;
    --contact-text: #dcdbe4;
    --brand-navy: #1c2a5c;
  }
  * { margin: 0; padding: 0; box-sizing: border-box; }
  html, body { width: 1200px; height: 900px; overflow: hidden; }
  body {
    background: var(--page-bg);
    font-family: "Lato", sans-serif;
    position: relative;
  }
  .business-card {
    position: absolute;
    left: 75px; top: 150px;
    width: 1050px; height: 600px;
    border-radius: 22px;
    overflow: hidden;
    box-shadow: 0 10px 30px rgba(30, 35, 60, 0.18);
  }
  .card-backdrop { position: absolute; inset: 0; }
  .holder-name {
    position: absolute;
    left: 40px; top: 236px;
    font-size: 35px;
    font-weight: 700;
    letter-spacing: 1.5px;
    color: var(--name-cream);
  }
  .contact-list {
    position: absolute;
    left: 40px; top: 296px;
    list-style: none;
  }
  .contact-item {
    display: flex;
    align-items: center;
    height: 32px;
    font-size: 24px;
    color: var(--contact-text);
    letter-spacing: 0.5px;
  }
  .contact-item.email { font-size: 21px; }
  .contact-icon { width: 18px; height: 18px; margin-right: 14px; flex: none; }
  .brand-name {
    position: absolute;
    left: 741px; top: 301px;
    transform: translate(-50%, -50%);
    font-size: 50px;
    font-weight: 900;
    color: var(--brand-navy);
    white-space: nowrap;
  }
</style>
</head>
<body>
  <section class="business-card">
    <svg class="card-backdrop" width="1050" height="600" viewBox="0 0 1050 600">
      <defs>
        <linearGradient id="navyPanel" x1="0" y1="0" x2="1" y2="0">
          <stop offset="0" stop-color="#3f4c7e"/>
          <stop offset="0.3" stop-color="var(--navy-soft)"/>
          <stop offset="0.6" stop-color="var(--navy-deep)"/>
          <stop offset="0.85" stop-color="var(--navy-mid)"/>
          <stop offset="1" stop-color="var(--navy-soft)"/>
        </linearGradient>
      </defs>
      <rect width="1050" height="600" fill="url(#navyPanel)"/>
      <path d="M640 0 H1050 V600 H700 C580 560 520 420 560 260 C580 160 610 60 640 0 Z" fill="var(--panel-light)"/>
      <circle cx="741" cy="301" r="312" fill="var(--ring-white)"/>
      <circle cx="741" cy="301" r="300" fill="var(--disc-grey)"/>
    </svg>

    <h1 class="holder-name">FAISAL QURESHI</h1>
    <ul class="contact-list">
      <li class="contact-item">
        <svg class="contact-icon" viewBox="0 0 24 24"><path fill="var(--contact-text)" d="M6.6 10.8a15.1 15.1 0 0 0 6.6 6.6l2.2-2.2a1 1 0 0 1 1-.25 11.4 11.4 0 0 0 3.6.57 1 1 0 0 1 1 1V20a1 1 0 0 1-1 1A17 17 0 0 1 3 4a1 1 0 0 1 1-1h3.5a1 1 0 0 1 1 1c0 1.25.2 2.45.57 3.57a1 1 0 0 1-.25 1z"/></svg>
        413-719-4820
      </li>
      <li class="contact-item">
        <svg class="contact-icon" viewBox="0 0 24 24"><rect x="6" y="2" width="12" height="20" rx="2" fill="none" stroke="var(--contact-text)" stroke-width="2"/><circle cx="12" cy="18" r="1.2" fill="var(--contact-text)"/></svg>
        413-585-2046
      </li>
      <li class="contact-item email">
        <svg class="contact-icon" viewBox="0 0 24 24"><rect x="2" y="5" width="20" height="14" rx="1.5" fill="var(--contact-text)"/><path d="M2.5 6 12 13l9.5-7" fill="none" stroke="var(--navy-soft)" stroke-width="1.6"/></svg>
        Brooksidegrocer512@fernpost.com
      </li>
    </ul>

    <div class="brand-name">Brookside Grocer</div>
  </section>
</body>
</html>
```